Data/Computer Security company needs a brochure design

We need a brochure design for Vaultmere Lens.
We deliver security solutions that manage critical risks, protect vital information and provide regulatory compliance. (mostly professional offices and small businesses with an emphasis in financial services) Optimal security is achieved through agent-based auditing and network activity monitoring.
Specialists in the area of helping Broker/Dealers and Independent Financial Service Representatives measure field office security, threat readiness and compliance with current policies and procedures. We provide auditors with clear, concise reports of policy deviations along with guidance in closing gaps, weaknesses or deficiencies.
Our services allow audit staff efficiency and productivity in their process while ensuring the field offices are utilizing best security practices and exercising the appropriate level of diligence and care in protecting the client information entrusted to them.
More about process and services can be seen on our website - www.vaultmerelens.example
We use blues and grays in our designs.
Financial

```html
<!DOCTYPE html>
<html lang="en">
<head>
<meta charset="utf-8">
<title>Vaultmere Lens – Brochure</title>
<link rel="stylesheet" href="https://fonts.googleapis.com/css2?family=Lato:wght@300;400;700;900&family=Open+Sans:wght@800&display=swap">
<style>
  :root {
    --brand-blue: #23399b;
    --cover-black: #231f20;
    --panel-gray: #eceeed;
    --text-gray: #4a4a4a;
    --navy-dark: #0b1433;
    --navy-light: #2c3d74;
    --white: #ffffff;
  }
  * { box-sizing: border-box; margin: 0; padding: 0; }
  html, body { width: 960px; height: 1200px; overflow: hidden; background: var(--white); }
  body { position: relative; font-family: "Lato", sans-serif; color: var(--text-gray); }

  .sheet {
    position: absolute; width: 866px; height: 560px; background: var(--white);
    box-shadow: 3px 3px 5px rgba(0,0,0,0.35); border: 1px solid #d8d8d8; overflow: hidden;
  }
  .sheet--cover { left: 22px; top: 24px; }
  .sheet--inside { left: 70px; top: 616px; }
  .sheet__art { position: absolute; inset: 0; width: 100%; height: 100%; }

  /* Cover */
  .cover-photos { position: absolute; left: 571px; top: 208px; width: 160px; border-top: 1px solid #9a9a9a; padding-top: 3px; display: flex; gap: 5px; }
  .cover-photos__tile { flex: 1; height: 32px; background: linear-gradient(135deg, #dfe3ec, #6f7990 60%, #2f3546); }
  .cover-tagline { position: absolute; left: 571px; top: 250px; width: 160px; color: var(--white); font-size: 8.4px; letter-spacing: 1.9px; line-height: 9.4px; text-transform: uppercase; border-bottom: 1px solid #c9c9c9; padding-bottom: 2px; white-space: nowrap; }
  .cover-tagline strong { font-weight: 900; }
  .brand-name { position: absolute; left: 32px; top: 438px; display: flex; align-items: center; gap: 5px; color: var(--brand-blue); font-weight: 900; font-size: 13px; }
  .brand-name__dot { width: 9px; height: 9px; border-radius: 50%; background: var(--brand-blue); }
  .contact { position: absolute; left: 33px; top: 484px; font-size: 6.4px; line-height: 9.2px; color: var(--text-gray); }
  .contact__web { color: var(--brand-blue); margin-top: 3px; font-size: 7px; }

  /* Inside */
  .intro { position: absolute; left: 22px; top: 53px; width: 400px; font-family: "Open Sans", sans-serif; font-weight: 800; font-size: 9.3px; line-height: 12px; color: var(--brand-blue); }
  .column { position: absolute; font-size: 5.9px; line-height: 7.3px; font-weight: 300; color: #333; }
  .column--facts { left: 0; top: 102px; width: 210px; height: 396px; background: var(--panel-gray); padding: 17px 14px 0 22px; }
  .column--services { left: 222px; top: 117px; width: 190px; }
  .column--services-cont { left: 463px; top: 127px; width: 182px; }
  .section-title { color: var(--brand-blue); font-size: 7.2px; font-weight: 400; text-transform: uppercase; margin: 0 0 1px; letter-spacing: -0.1px; }
  .section-title + p, .column p { margin-bottom: 4px; }
  .fact-list { list-style: none; margin-bottom: 7px; }
  .fact-list li { position: relative; padding-left: 8px; margin-bottom: 3px; }
  .fact-list li::before { content: "•"; position: absolute; left: 0; }
  .service-list { list-style: none; counter-reset: svc; }
  .service-list li { position: relative; padding-left: 8px; margin-bottom: 4px; }
  .service-list li::before { position: absolute; left: 0; font-weight: 700; content: attr(data-n); }
  .service-list strong { font-weight: 400; }
  .pricing { position: absolute; left: 455px; top: 357px; width: 196px; height: 80px; background: var(--panel-gray); padding: 7px 9px; font-size: 6.2px; line-height: 7.6px; font-weight: 300; color: #333; }
  .pricing__fee { font-weight: 900; font-size: 7px; color: #222; }
  .pricing p { margin-bottom: 3px; }
</style>
</head>
<body>

<section class="sheet sheet--cover" aria-label="Brochure cover">
  <svg class="sheet__art" viewBox="0 0 866 560" preserveAspectRatio="none" aria-hidden="true">
    <path d="M384 0 C414 180 414 400 382 560 L866 560 L866 0 Z" fill="var(--cover-black)"/>
    <path d="M352 0 L380 0 C410 180 410 400 378 560 L350 560 C380 400 382 180 352 0 Z" fill="var(--brand-blue)"/>
  </svg>
  <div class="cover-photos">
    <div class="cover-photos__tile" role="img" aria-label="Photo of hands typing on a laptop"></div>
    <div class="cover-photos__tile" role="img" aria-label="Photo of office towers seen from below"></div>
    <div class="cover-photos__tile" role="img" aria-label="Photo of a pen signing a document"></div>
  </div>
  <p class="cover-tagline">Protecting your clients,<br>protecting your business<br>computer security solutions<br>from <strong>Vaultmere Lens</strong></p>
  <div class="brand-name"><span class="brand-name__dot"></span>Vaultmere Lens</div>
  <address class="contact" style="font-style:normal">
    4870 Harborview Rd<br>Suite B22<br>Ashford, IA 50999<br>(555) 014 2290
    <div class="contact__web">www.vaultmerelens.example</div>
  </address>
</section>

<section class="sheet sheet--inside" aria-label="Brochure inside spread">
  <svg class="sheet__art" viewBox="0 0 866 560" preserveAspectRatio="none">
    <defs>
      <linearGradient id="codeGlow" x1="0" y1="0" x2="1" y2="1">
        <stop offset="0" stop-color="var(--navy-dark)"/>
        <stop offset="0.55" stop-color="var(--navy-light)"/>
        <stop offset="1" stop-color="var(--navy-dark)"/>
      </linearGradient>
    </defs>
    <path role="img" aria-label="Image of streaming code with words like virus, worm, spam, spyware and phishing" d="M697 0 C729 170 729 380 697 560 L866 560 L866 0 Z" fill="url(#codeGlow)"/>
    <path d="M674 0 L692 0 C724 170 724 380 692 560 L674 560 C706 380 706 170 674 0 Z" fill="var(--brand-blue)"/>
  </svg>

  <p class="intro">Cybercrime and privacy concerns are an ever-growing business threat and Vaultmere Lens has a series of affordable, actionable steps to help protect both you and your clients.</p>

  <div class="column column--facts">
    <h2 class="section-title">How big is the problem?</h2>
    <ul class="fact-list">
      <li>Anti-virus vendors report receiving 60,000 new malware samples every day</li>
      <li>Approximately 1500 new malware sites are created per day</li>
      <li>Sixty-percent of top Findwell search terms return malicious sites within the first 100 results</li>
    </ul>
    <h2 class="section-title">Why do they do it?</h2>
    <ul class="fact-list">
      <li>Northpill Pharmacy spam campaign can net $16,000 per day</li>
      <li>Affiliate webmaster redirecting to a scareware site can net $180,000 a year</li>
      <li>Credit card information sells for $15 to $200 (at the higher end if it includes the PIN)</li>
      <li>Botnet rental runs as little as $10-$65 per hour</li>
      <li>One million e-mail addresses can be purchased for $20-$100</li>
      <li>Complete set of data on a US resident is only $5 to $8</li>
      <li>A continuous 24-hour Botnet for DDoS attacks can be launched for as little as $50</li>
      <li>Stolen bank account details go for $1 to $1,500 depending on level of detail and balance</li>
    </ul>
    <h2 class="section-title">How do they do it?</h2>
    <p>They do it by exploiting weaknesses in common software like Webline Browser, Deskwork Suite, PaperView Reader, Flicker Player and Kova Runtime. Software developers have created 'crimeware' applications designed to exploit known weaknesses in software on the target computers. The malware is delivered in numerous ways:</p>
    <ul class="fact-list">
      <li>A pop-up in your web browser saying you have a virus</li>
      <li>In a pdf or poisoned Deskwork Suite email attachment</li>
      <li>A link in a Friendloop message</li>
      <li>A link in your Findwell search results</li>
      <li>A contaminated USB drive</li>
      <li>Inside a free game or download</li>
      <li>Poisoned ads on prominent websites</li>
      <li>Through security weaknesses in old, un-patched software</li>
    </ul>
  </div>

  <div class="column column--services">
    <h2 class="section-title">How we help you protect yourself</h2>
    <p>Vaultmere Lens's five-point program helps you understand and manage your risks. Protecting your business need not be burdensome, time consuming or expensive.</p>
    <ol class="service-list">
      <li data-n="1."><strong>Patch Management</strong> – Utilizing the same tools used by the Military, we monitor the applications installed on each computer daily. We compare this list to known vulnerabilities and updates. If any of your applications are at risk, we notify you and provide instructions on how to update the appropriate application.</li>
      <li data-n="2."><strong>New Application Monitoring</strong> – All newly installed applications are screened for suitability and consistency. You are notified of any new applications installed which seem to be out of the ordinary. In many cases, we are able to identify malware soon after it has been installed. We also help catch non-approved user installed applications.</li>
      <li data-n="3."><strong>Anti-Virus Monitoring</strong> – Daily, each computer is checked for functioning and up-to-date Anti-virus software.</li>
      <li data-n="4."><strong>Realtime Internet Navigation and Security Services</strong> – Comprehensive security for your network through award-winning phishing, botnet and malware site protection. Our Web filtering service delivers network security services through the DNS layer blocking known malicious or infected sites from resolving on your network. Since infected sites are prevented from resolving, phishing attempts and malicious content are blocked from reaching your network thereby providing the most efficient protection available.
        <p style="margin-top:4px">If one of your computers did become infected, built-in botnet protection stops trojans, key loggers, and other persistent malware and viruses on machines in your network from sending out confidential data and personal information to hackers outside the firewall. We will alert you if we detect certain botnets on your network to enable you to take immediate action.</p>
      </li>
    </ol>
  </div>

  <div class="column column--services-cont">
    <p>Malware site protection stops users from unknowingly going to known sites that can infect user machines, typically through the use of drive-by downloads and browser vulnerabilities. This prevents infected content from reaching your network where it can cause harm and spread to other machines. Our list of hundreds of thousands of known bad Web addresses is updated every five minutes to provide you with the most up-to-date protection.</p>
    <p>Web content filtering is also provided, allowing access to a rich database of more than 50 categories and millions of domains. This allows you to control which sites can be accessed on your network. The ability to set content filtering policies on a per-site or per-network basis, giving you greater control when applying access policies to Internet usage.</p>
    <ol class="service-list">
      <li data-n="5."><strong>Security Awareness Program</strong> – Your staff can be one of your greatest strengths or an easily exploitable weakness. Cybercriminals prey on the untrained to gain access. We provide a program to help educate your staff on techniques currently in use by cybercriminals and how to best deal with these threats. This program is delivered through short, weekly emailed security briefings; each taking no more than two minutes to read.</li>
    </ol>
  </div>

  <div class="pricing">
    <h2 class="section-title">Pricing</h2>
    <p class="pricing__fee">Monthly fee of $13.50 per computer.</p>
    <p>Sales tax may be applicable in some areas.</p>
    <p>With Vaultmere Lens's unique services, the security of personal and confidential information does not need to be burdensome, intrusive or expensive.</p>
  </div>
</section>

</body>
</html>
```